Need Letterhead and Business Card

I have a logo but i need new letterhead and biz cards. We are a real estate investment firm so we need very professional but also do not want to be old fashioned. We have 3 locations; Singapore, New York and Ponte Vedra Florida. I can provide full addresses if needed. If you have adjustments to our logo you would recommend we are open to them.
I will be putting in a separate project but we also need a template for our own powerpoint slide presentations and website.

Real Estate

```html
<!DOCTYPE html>
<html lang="en">
<head>
<meta charset="utf-8">
<title>Halden Business Card – Front and Back</title>
<link rel="stylesheet" href="https://fonts.googleapis.com/css2?family=Exo+2:wght@300;400;600;700&display=swap">
<style>
  :root {
    --stage: #231f20;
    --navy: #074d85;
    --gold: #c9a031;
    --paper: #ffffff;
    --ink-grey: #8a8a8a;
    --label: #f2f2f2;
  }
  * { margin: 0; padding: 0; box-sizing: border-box; }
  html, body {
    width: 1200px; height: 1000px; overflow: hidden;
    background: var(--stage);
    font-family: "Exo 2", sans-serif;
  }
  .canvas { position: relative; width: 1200px; height: 1000px; }

  .card {
    position: absolute; left: 304px; width: 587px; height: 357px;
    border-radius: 18px; overflow: hidden; background: var(--paper);
  }
  .card--front { top: 65px; }
  .card--back { top: 535px; }

  .card__edge-bar {
    position: absolute; left: 0; top: 75px; width: 8px; height: 164px;
    background: var(--navy);
  }
  .card__band {
    position: absolute; left: 0; right: 0; bottom: 0; height: 45px;
    background: var(--navy);
    display: flex; align-items: center; justify-content: center;
  }
  .card__web {
    font-size: 15px; font-weight: 300; letter-spacing: 3px;
  }
  .card__band .card__web { color: var(--label); }

  .brand {
    position: absolute; display: flex; align-items: center;
    font-weight: 600; color: var(--navy);
  }
  .brand__mark { display: block; background: currentColor; }
  .card--front .brand { left: 30px; top: 140px; font-size: 46px; gap: 10px; letter-spacing: 1px; }
  .card--front .brand__mark { width: 14px; height: 14px; }

  .holder { position: absolute; left: 305px; top: 92px; }
  .holder__name { font-size: 18px; font-weight: 600; color: var(--navy); line-height: 19px; }
  .holder__title { font-size: 16px; font-weight: 600; color: var(--gold); line-height: 17px; }

  .contact { position: absolute; left: 294px; top: 156px; list-style: none; }
  .contact__item {
    display: flex; align-items: flex-start; gap: 8px;
    font-size: 14px; font-weight: 300; color: var(--ink-grey); line-height: 17px;
  }
  .contact__icon { width: 18px; height: 17px; flex: none; fill: var(--gold); }

  .card--back .card__face {
    position: absolute; left: 0; right: 0; top: 0; height: 312px; background: var(--navy);
  }
  .card--back .brand {
    left: 0; right: 0; top: 110px; justify-content: center;
    color: var(--paper); font-size: 82px; gap: 16px; letter-spacing: 2px;
  }
  .card--back .brand__mark { width: 22px; height: 22px; }
  .card__foot {
    position: absolute; left: 0; right: 0; bottom: 0; height: 45px;
    display: flex; align-items: center; justify-content: center;
  }
  .card__foot .card__web { color: var(--navy); }

  .caption {
    position: absolute; width: 300px; text-align: center;
    font-size: 30px; font-weight: 400; color: var(--label);
  }
  .caption--front { left: 443px; top: 446px; }
  .caption--back { left: 460px; top: 908px; }
</style>
</head>
<body>
<main class="canvas">

  <section class="card card--front" aria-label="Business card front">
    <div class="card__edge-bar"></div>
    <div class="brand"><span class="brand__mark"></span><span class="brand__name">HALDEN</span></div>

    <div class="holder">
      <p class="holder__name">Cardholder’s Name</p>
      <p class="holder__title">Job Tittle</p>
    </div>

    <ul class="contact">
      <li class="contact__item">
        <svg class="contact__icon" viewBox="0 0 18 17" aria-hidden="true"><path d="M9 2 1 9h2.5v6h4v-4h3v4h4V9H17z"/></svg>
        <span>9999, Address Line, Your City, Your<br>State , Zip Code - 100 001</span>
      </li>
      <li class="contact__item">
        <svg class="contact__icon" viewBox="0 0 18 17" aria-hidden="true"><rect x="5" y="1" width="7" height="15" rx="1.5"/><rect x="6.5" y="3" width="4" height="6" fill="#fff"/></svg>
        <span>+ 123.456.789</span>
      </li>
      <li class="contact__item">
        <svg class="contact__icon" viewBox="0 0 18 17" aria-hidden="true"><rect x="5" y="2" width="8" height="5"/><rect x="2" y="7" width="14" height="8" rx="1"/></svg>
        <span>+ 123.456.789</span>
      </li>
      <li class="contact__item">
        <svg class="contact__icon" viewBox="0 0 18 17" aria-hidden="true"><path d="M5 2c-2 1-3 4-1 8s5 6 7 5l1-1-2-3-2 1c-1-1-2-3-2-4l2-1-1-3z"/></svg>
        <span>+ 123.456.789</span>
      </li>
      <li class="contact__item">
        <svg class="contact__icon" viewBox="0 0 18 17" aria-hidden="true"><rect x="2" y="5" width="13" height="8" rx="1"/></svg>
        <span>info@companyname.com</span>
      </li>
    </ul>

    <div class="card__band"><span class="card__web">www.companyname.com</span></div>
  </section>

  <p class="caption caption--front">Front Card</p>

  <section class="card card--back" aria-label="Business card back">
    <div class="card__face"></div>
    <div class="brand"><span class="brand__mark"></span><span class="brand__name">HALDEN</span></div>
    <div class="card__foot"><span class="card__web">www.companyname.com</span></div>
  </section>

  <p class="caption caption--back">Back Card</p>

</main>
</body>
</html>
```